Software Engineering Company need eye catching banner for and Engineering conventions

We need an eye-catching banner designed. The size of the banner will be 34" W x 81" H. We develop routing software installed in bus systems and use GPS real-time tracking to always know where they are. We would like the banner to be dominated by the colors in our logo, 2 different blues, dark gray and of course white and black if needed. We are hoping for something that will pop out and look awesome. If you want to use our entire name or just our logo is completely up to you.

Target Market(s)

Young Engineers looking for new and cutting edge job opportunities

Industry/Entity Type

Computer Software

Colors
1f68ae
3779b6
ffffff

Requirements
Should not have
• the colors in our logo

```html
<!DOCTYPE html>
<html lang="en">
<head>
<meta charset="utf-8">
<title>Vantro Technologies – Future Forward Banner</title>
<link href="https://fonts.googleapis.com/css2?family=Montserrat:wght@500;600;700&family=Roboto+Condensed:wght@400;700&family=Noto+Serif:wght@400&display=swap" rel="stylesheet">
<style>
  :root {
    --blue-main: #1f68ae;
    --blue-light: #3779b6;
    --blue-deep: #0d4a8a;
    --blue-bright: #1e8fd6;
    --navy: #0f2f5e;
    --label-navy: #13386b;
    --gray-dark: #5f5f5f;
    --white: #ffffff;
    --cloud-gray: #e4e6ea;
  }
  * { box-sizing: border-box; margin: 0; padding: 0; }
  html, body { width: 686px; height: 1200px; overflow: hidden; background: #ffffff; }
  .banner {
    position: relative;
    width: 686px;
    height: 1200px;
    overflow: hidden;
    background: linear-gradient(180deg, var(--blue-main) 0%, #1a5fa3 50%, var(--blue-deep) 100%);
    font-family: "Roboto Condensed", "Arial Narrow", sans-serif;
    color: var(--white);
  }

  /* Header brand tab */
  .brand-tab {
    position: absolute;
    left: 132px; top: 0;
    width: 422px; height: 141px;
  }
  .brand-tab svg { position: absolute; inset: 0; }
  .brand-name {
    position: absolute;
    left: 0; right: 0; top: 26px;
    display: flex; align-items: center; justify-content: center; gap: 12px;
  }
  .brand-square {
    width: 34px; height: 34px;
    background: var(--blue-main);
  }
  .brand-wordmark {
    font-family: "Montserrat", sans-serif;
    font-weight: 700;
    font-size: 22px;
    line-height: 1.05;
    letter-spacing: 1.5px;
    color: var(--blue-main);
  }
  .brand-url {
    position: absolute;
    left: 0; right: 0; top: 84px;
    text-align: center;
    font-family: "Montserrat", sans-serif;
    font-weight: 500;
    font-size: 9.5px;
    letter-spacing: 3px;
    color: var(--navy);
  }

  /* Devices & cloud illustration area */
  .devices-art {
    position: absolute;
    left: 34px; top: 148px;
    width: 613px; height: 284px;
    border-radius: 14px;
    background: radial-gradient(ellipse at 45% 55%, rgba(255,255,255,0.16), rgba(255,255,255,0.04) 70%);
  }

  /* Headline */
  .rule {
    position: absolute;
    left: 68px; width: 550px; height: 14px;
  }
  .rule-top { top: 449px; }
  .rule-bottom { top: 527px; }
  .headline {
    position: absolute;
    left: 0; right: 0; top: 462px;
    text-align: center;
    font-family: "Noto Serif", "Times New Roman", serif;
    font-weight: 400;
    font-size: 51px;
    line-height: 60px;
    letter-spacing: 0.5px;
  }
  .tagline {
    position: absolute;
    left: 0; right: 0; top: 551px;
    text-align: center;
    font-family: "Montserrat", sans-serif;
    font-weight: 600;
    font-size: 13.6px;
    line-height: 21px;
  }

  .lower-panel {
    position: absolute;
    left: 0; top: 596px;
    width: 686px; height: 604px;
  }

  /* Feature rows */
  .feature-band {
    position: absolute;
    height: 30px;
    background: var(--white);
    color: var(--label-navy);
    font-family: "Roboto Condensed", sans-serif;
    font-weight: 700;
    font-size: 21px;
    line-height: 30px;
  }
  .band-left { left: 0; padding-left: 28px; }
  .band-right { right: 0; text-align: center; }
  .feature-badge {
    position: absolute;
    width: 84px; height: 76px;
    border-radius: 50%;
    background: var(--white);
    display: flex; align-items: center; justify-content: center;
  }
  .feature-text {
    position: absolute;
    font-size: 14.2px;
    line-height: 17px;
    color: var(--white);
  }

  /* Footer */
  .footer-clouds {
    position: absolute;
    left: 0; top: 1020px;
    width: 686px; height: 180px;
    background: linear-gradient(180deg, rgba(255,255,255,0) 0%, var(--cloud-gray) 35%, var(--white) 75%);
  }
  .call-bar {
    position: absolute;
    left: 167px; top: 1142px;
    width: 519px; height: 33px;
    background: var(--navy);
    border-radius: 17px 0 0 17px;
    font-family: "Roboto Condensed", sans-serif;
    font-weight: 700;
    font-size: 27px;
    line-height: 33px;
    text-align: center;
    letter-spacing: 0.3px;
    color: var(--white);
  }
</style>
</head>
<body>
<main class="banner">

  <header class="brand-tab">
    <svg width="422" height="141" viewBox="0 0 422 141" aria-hidden="true">
      <polygon points="0,0 422,0 422,141 212,107 0,141" fill="#ffffff"/>
      <polyline points="26,141 212,105 396,141" fill="none" stroke="#5f5f5f" stroke-width="4"/>
    </svg>
    <div class="brand-name">
      <span class="brand-square"></span>
      <span class="brand-wordmark">VANTRO<br>TECHNOLOGIES LLC</span>
    </div>
    <div class="brand-url">www.vantrotechnologies.com</div>
  </header>

  <div class="devices-art" role="img" aria-label="Outline illustration of a cloud surrounded by a phone, a tablet, a desktop monitor and a security shield"></div>

  <svg class="rule rule-top" viewBox="0 0 550 14" aria-hidden="true">
    <line x1="8" y1="7" x2="542" y2="7" stroke="#ffffff" stroke-width="1.5"/>
    <circle cx="8" cy="7" r="6" fill="#ffffff"/><circle cx="542" cy="7" r="6" fill="#ffffff"/>
  </svg>
  <h1 class="headline">FUTURE FORWARD</h1>
  <svg class="rule rule-bottom" viewBox="0 0 550 14" aria-hidden="true">
    <line x1="8" y1="7" x2="542" y2="7" stroke="#ffffff" stroke-width="1.5"/>
    <circle cx="8" cy="7" r="6" fill="#ffffff"/><circle cx="542" cy="7" r="6" fill="#ffffff"/>
  </svg>
  <p class="tagline">We develop routing software installed in bus systems and<br>use GPS real-time tracking to always know where they are.</p>

  <svg class="lower-panel" viewBox="0 0 686 604" aria-hidden="true">
    <polygon points="0,0 343,18 686,0 686,604 0,604" fill="#0e4a8a" opacity="0.55"/>
  </svg>

  <!-- Technology -->
  <div class="feature-band band-left" style="top:667px;width:220px;">TECHNOLOGY</div>
  <div class="feature-badge" style="left:199px;top:642px;">
    <svg width="52" height="40" viewBox="0 0 52 40" aria-hidden="true">
      <rect x="7" y="12" width="32" height="20" rx="2" fill="none" stroke="#13386b" stroke-width="3"/>
      <path d="M2 34 H44 L41 38 H5 Z" fill="#13386b"/>
      <rect x="38" y="2" width="8" height="6" fill="#13386b"/>
      <rect x="30" y="8" width="6" height="5" fill="#13386b"/>
      <rect x="24" y="16" width="5" height="4" fill="#13386b"/>
      <rect x="31" y="20" width="4" height="4" fill="#13386b"/>
      <rect x="18" y="22" width="4" height="3" fill="#13386b"/>
    </svg>
  </div>
  <p class="feature-text" style="left:316px;top:645px;width:350px;">We implement the latest innovations in transportation technology. This gives us the ability to provide you with reliable, accurate data when you need it most.</p>

  <!-- Cloud -->
  <p class="feature-text" style="left:34px;top:757px;width:360px;">We use state of the art cloud technology to store and process your day to day operations. Your data is always just a few clicks away.</p>
  <div class="feature-band band-right" style="top:777px;width:240px;padding-left:50px;">CLOUD</div>
  <div class="feature-badge" style="left:396px;top:754px;">
    <svg width="54" height="32" viewBox="0 0 54 32" aria-hidden="true">
      <path d="M10 30 A9 9 0 0 1 10 13 A14 14 0 0 1 36 9 A11 11 0 0 1 44 30 Z" fill="#13386b"/>
    </svg>
  </div>

  <!-- GPS -->
  <div class="feature-band band-left" style="top:875px;width:220px;padding-left:85px;">GPS</div>
  <div class="feature-badge" style="left:199px;top:851px;">
    <svg width="52" height="44" viewBox="0 0 52 44" aria-hidden="true">
      <path d="M3 32 L28 24 L49 32 L24 41 Z" fill="none" stroke="#13386b" stroke-width="2.5" stroke-linejoin="round"/>
      <path d="M26 30 C18 20 17 17 17 13 A9 9 0 0 1 35 13 C35 17 34 20 26 30 Z" fill="#13386b"/>
      <circle cx="26" cy="13" r="3.5" fill="#ffffff"/>
    </svg>
  </div>
  <p class="feature-text" style="left:316px;top:866px;width:350px;">GPS tracking gives you the real-time information necessary to keep your vehicles on the road and on-time.</p>

  <!-- Secure -->
  <p class="feature-text" style="left:34px;top:968px;width:360px;">With the latest security protocols in place, you can be rest assured that your data is safe.</p>
  <div class="feature-band band-right" style="top:979px;width:240px;padding-left:50px;">SECURE</div>
  <div class="feature-badge" style="left:398px;top:955px;">
    <svg width="36" height="42" viewBox="0 0 36 42" aria-hidden="true">
      <path d="M9 18 V12 A9 9 0 0 1 27 12 V18" fill="none" stroke="#13386b" stroke-width="4.5"/>
      <rect x="3" y="18" width="30" height="22" rx="3" fill="#13386b"/>
      <circle cx="18" cy="27" r="3" fill="#ffffff"/>
      <rect x="16.5" y="28" width="3" height="6" fill="#ffffff"/>
    </svg>
  </div>

  <!-- Footer -->
  <div class="footer-clouds" role="img" aria-label="Soft white and light gray clouds along the bottom edge"></div>
  <div class="call-bar">CALL US TODAY - 555.014.2870</div>

</main>
</body>
</html>
```